Business Card for Quillmark Ledger - A cannabis publication for executives.

I'd like some business cards for Quillmark Ledger. The logo is done (great job!) and I need a card design I will use with PRINTLY. I made it a short project to allow time for printing before an event. These will be standard sized cards (final artwork size 3.66" x 2.16" at 300dpi) with a final card size of 3.5" x 2.0". (See PRINTLY.com if you need more info.) I might try rounded corners but am not sure yet. I think the design will work okay with rounded.

Quillmark Ledger will be a bi-weekly publication for the cannabis industry. It is targeted to investors and industry executives, not consumers or pot smokers. So our market is more B2B. However I am open to creativity and making the card something people remark on.

My contact for card:

Dana Merrow
Founder/CEO
dana@quillmarkledger.example

2740 Harlow Avenue
Boston MA 02135
(617)555-0194

Target Market(s)

Executives, Industry people and investors in the Cannabis sector.

Contact Information for Business Card

PRINTLY does do double sided and the second side can be the same or different images. Only one side is required but use of the second side would be a bonus.

Font styles to use
Serif
Sans Serif
Decorative

Colors

Designer to choose colors to be used in the design.

Requirements
Must have
• Logo, contact info
Nice to have
• Style and design to make the card stand out in a crowd.

```html
<!DOCTYPE html>
<html lang="en">
<head>
<meta charset="utf-8">
<title>Quillmark Ledger – Business Card</title>
<link href="https://fonts.googleapis.com/css2?family=Source+Sans+3:wght@400;600&display=swap" rel="stylesheet">
<style>
  :root {
    --bg: #ebe9e9;
    --card: #ffffff;
    --green: #82a53a;
    --blue: #456ba5;
    --pattern: #f7f6f6;
  }
  * { margin: 0; padding: 0; box-sizing: border-box; }
  html, body { width: 1200px; height: 1200px; overflow: hidden; }
  body {
    position: relative;
    background: var(--bg);
    font-family: "Source Sans 3", "Myriad Pro", Arial, sans-serif;
  }
  .card {
    position: absolute;
    background: var(--card);
    box-shadow: 0 10px 8px -8px rgba(0,0,0,0.45);
  }
  .card svg.card-shapes { position: absolute; inset: 0; display: block; }
  .card-front { left: 231px; top: 123px; width: 731px; height: 431px; }
  .card-back  { left: 230px; top: 667px; width: 726px; height: 439px; }

  .brand-pattern {
    position: absolute; left: 40px; top: 95px; width: 651px; height: 260px;
    background: var(--pattern);
  }
  .brand {
    position: absolute;
    display: flex; align-items: center;
    color: var(--blue);
    font-weight: 600;
    white-space: nowrap;
  }
  .brand-mark { border-radius: 50%; background: var(--green); flex: none; }
  .brand-front { left: 143px; top: 170px; font-size: 46px; gap: 14px; }
  .brand-front .brand-mark { width: 76px; height: 76px; }
  .brand-back { left: 64px; top: 182px; font-size: 28px; gap: 10px; }
  .brand-back .brand-mark { width: 46px; height: 46px; }

  .person {
    position: absolute; left: 434px; width: 240px; top: 96px;
    text-align: center;
  }
  .person-name { color: var(--blue); font-size: 35px; font-weight: 400; line-height: 1.1; }
  .person-title { color: var(--green); font-size: 18px; margin-top: 6px; }

  .contact-list { position: absolute; left: 415px; top: 208px; list-style: none; }
  .contact-item {
    position: absolute; left: 0; display: flex; align-items: flex-start; gap: 12px;
    color: var(--blue); font-size: 19px; line-height: 25px; white-space: nowrap;
  }
  .contact-icon { width: 28px; height: 28px; flex: none; }
  .contact-item.phone   { top: 0; }
  .contact-item.email   { top: 47px; }
  .contact-item.address { top: 96px; }
  .contact-item.web     { top: 157px; }
</style>
</head>
<body>

<section class="card card-front" aria-label="Business card front">
  <div class="brand-pattern" role="img" aria-label="Faint repeated brand pattern"></div>
  <svg class="card-shapes" viewBox="0 0 914 539" preserveAspectRatio="none" aria-hidden="true">
    <polygon fill="var(--green)" points="0,0 914,0 914,96 874,71 840,71 800,96 760,71 734,71 694,96 654,71 627,71 587,96 547,71 521,71 481,96 441,71 414,71 374,96 334,71 308,71 268,96 228,71 202,71 162,96 122,71 96,71 56,96 16,71 0,71"/>
    <polygon fill="var(--blue)" points="0,539 0,473 16,473 56,448 96,473 122,473 162,448 202,473 228,473 268,448 308,473 334,473 374,448 414,473 441,473 481,448 521,473 547,473 587,448 627,473 654,473 694,448 734,473 760,473 800,448 840,473 874,473 914,448 914,539"/>
  </svg>
  <div class="brand brand-front"><span class="brand-mark"></span><span class="brand-name">Quillmark Ledger</span></div>
</section>

<section class="card card-back" aria-label="Business card back">
  <svg class="card-shapes" viewBox="0 0 908 549" preserveAspectRatio="none" aria-hidden="true">
    <polygon fill="var(--blue)" points="548,4 846,4 796,94 600,94"/>
    <polygon fill="var(--green)" points="133,464 331,464 378,549 86,549"/>
  </svg>

  <div class="brand brand-back"><span class="brand-mark"></span><span class="brand-name">Quillmark Ledger</span></div>

  <div class="person">
    <p class="person-name">Dana Merrow</p>
    <p class="person-title">Founder/CEO</p>
  </div>

  <ul class="contact-list">
    <li class="contact-item phone">
      <svg class="contact-icon" viewBox="0 0 28 28" aria-hidden="true"><circle cx="14" cy="14" r="14" fill="var(--green)"/><path d="M9.5 7.5l2.5-.5 1.5 3.5-1.8 1.2a8 8 0 0 0 4.1 4.1l1.2-1.8 3.5 1.5-.5 2.5c-5.5.6-11-4.9-10.5-10.5z" fill="#fff"/></svg>
      <span>(617)555-0194</span>
    </li>
    <li class="contact-item email">
      <svg class="contact-icon" viewBox="0 0 28 28" aria-hidden="true"><circle cx="14" cy="14" r="14" fill="var(--green)"/><rect x="7.5" y="9.5" width="13" height="9" fill="#fff"/><path d="M7.5 9.5l6.5 5 6.5-5M7.5 18.5l5-4.2M20.5 18.5l-5-4.2" stroke="var(--green)" stroke-width="1.2" fill="none"/></svg>
      <span>dana@quillmarkledger.example</span>
    </li>
    <li class="contact-item address">
      <svg class="contact-icon" viewBox="0 0 28 28" aria-hidden="true"><circle cx="14" cy="14" r="14" fill="var(--green)"/><path d="M14 22s-5.5-6-5.5-9.5a5.5 5.5 0 0 1 11 0C19.5 16 14 22 14 22z" fill="#fff"/><circle cx="14" cy="12.5" r="2" fill="var(--green)"/></svg>
      <span>2740 Harlow Avenue<br>Boston MA 02135</span>
    </li>
    <li class="contact-item web">
      <svg class="contact-icon" viewBox="0 0 28 28" aria-hidden="true"><circle cx="14" cy="14" r="14" fill="var(--green)"/><circle cx="14" cy="14" r="7" fill="#fff"/><path d="M10 10.5l2.5 1 .5 2.5-2 1.5-1.5-1.5zM15 16l3 .5-1 3-2.5-1z" fill="var(--green)"/></svg>
      <span>www.quillmarkledger.example</span>
    </li>
  </ul>
</section>

</body>
</html>
```